Quick and easy spring book cover needed

We need a creative book cover design for a spring fiction book. The title of the book is The Lantern Harbor Promise. The author's name is Gareth Holloway. The book is 4.25 x 7 inch. The spine is .5 inch. It should include the title, the author's name, and the emblem. The emblem should be set at .5 inches in length.
The book summary is as follows:
When Mira Dawson moves from her homeland in Japan to pursue her dream as an editor in the United States, she soon encounters a young Washingtonian artist. After being given the task to interview him, she becomes fixated on the mystique surrounding his past. She conjures her inner detective skills to embark on, what she thinks is, the biggest story of her career. But will her heart get in her way?
The final design should reflect spring and young love, nothing sexual and overly romantic. The background and font colors should go well with the imagery. I have attached 2 photos in which should be incorporated. The third attachment is the emblem that is to be placed at the bottom of the spine.

```html
<!DOCTYPE html>
<html lang="en">
<head>
<meta charset="utf-8">
<title>The Lantern Harbor Promise — Cover Spread</title>
<link rel="stylesheet" href="https://fonts.googleapis.com/css2?family=Emilys+Candy&family=PT+Sans+Narrow:wght@700&family=Source+Sans+3:ital,wght@0,400;0,600;1,600&display=swap">
<style>
  :root {
    --paper: #ffffff;
    --berry: #a3155f;
    --berry-deep: #7d0f48;
    --cream: #f6eeb4;
    --mist: #e9e9e9;
    --mist-dark: #b9b9b9;
    --bark: #6f665c;
    --bark-dark: #4c443d;
    --moss: #7f9a58;
    --spine-line: #e6e6e6;
  }
  * { margin: 0; padding: 0; box-sizing: border-box; }
  html, body { width: 1200px; height: 933px; overflow: hidden; background: var(--paper); }
  .spread { position: relative; width: 1200px; height: 933px; background: var(--paper); }

  .panel { position: absolute; top: 0; height: 933px; }
  .back-cover { left: 0; width: 565px; }
  .spine { left: 565px; width: 70px; border-left: 1px solid var(--spine-line); border-right: 1px solid var(--spine-line); }
  .front-cover { left: 635px; width: 565px; overflow: hidden; }

  .title-block { position: absolute; text-align: center; color: var(--berry); font-family: "Emilys Candy", cursive; }
  .title-block .title-small {
    display: block; font-family: "Source Sans 3", sans-serif; font-weight: 600;
    font-size: 15px; letter-spacing: 2px; color: var(--berry-deep);
  }
  .title-block .title-main {
    display: block; line-height: 1; color: var(--berry);
    -webkit-text-stroke: 1px var(--cream);
    text-shadow: 2px 3px 3px rgba(80, 20, 50, 0.35);
  }
  .back-cover .title-block { left: 70px; top: 40px; width: 400px; }
  .back-cover .title-main { font-size: 52px; margin: 4px 0 6px; }
  .front-cover .title-block { left: 40px; top: 125px; width: 485px; }
  .front-cover .title-main { font-size: 62px; margin: 6px 0 8px; }

  .synopsis {
    position: absolute; left: 70px; top: 205px; width: 485px;
    font-family: "Source Sans 3", sans-serif; font-style: italic; font-weight: 600;
    font-size: 19.5px; line-height: 43px; color: var(--berry);
  }

  .back-photo {
    position: absolute; left: 0; bottom: 0; width: 565px; height: 420px;
    background: linear-gradient(to bottom, var(--paper) 0%, var(--mist) 35%, var(--mist-dark) 75%, #cfcfcf 100%);
  }
  .front-photo {
    position: absolute; left: 0; bottom: 0; width: 565px; height: 565px;
    background:
      linear-gradient(to bottom, var(--paper) 0%, rgba(255,255,255,0) 32%),
      linear-gradient(to right, var(--moss) 0%, var(--bark) 22%, var(--bark) 70%, var(--bark-dark) 100%);
  }

  .spine-emblem {
    position: absolute; left: 0; top: 10px; width: 70px;
    display: flex; flex-direction: column; align-items: center; gap: 4px;
  }
  .spine-emblem .emblem-square { width: 10px; height: 10px; background: var(--berry); }
  .spine-emblem .emblem-name {
    writing-mode: vertical-rl; font-family: "Source Sans 3", sans-serif; font-weight: 600;
    font-size: 8px; letter-spacing: 1px; color: var(--berry);
  }
  .spine-author {
    position: absolute; left: 0; top: 110px; width: 70px; height: 300px;
    writing-mode: vertical-rl; text-align: center; line-height: 70px;
    font-family: "Source Sans 3", sans-serif; font-weight: 600; font-size: 14px;
    letter-spacing: 9px; color: var(--berry-deep); text-transform: uppercase;
  }
  .spine-title {
    position: absolute; left: 0; top: 548px; width: 70px; height: 340px;
    writing-mode: vertical-rl; text-align: left; line-height: 70px;
    font-family: "PT Sans Narrow", sans-serif; font-weight: 700; font-size: 28px;
    color: var(--berry);
  }

  .front-author {
    position: absolute; left: 0; bottom: 22px; width: 565px; text-align: center;
    font-family: "Source Sans 3", sans-serif; font-weight: 400; font-size: 15px;
    letter-spacing: 7px; color: var(--paper); text-transform: uppercase;
  }
</style>
</head>
<body>
<main class="spread">
  <section class="panel back-cover">
    <div class="back-photo" role="img" aria-label="Soft grey photo of blossoming trees with a young couple sitting on the grass"></div>
    <h2 class="title-block">
      <span class="title-small">THE</span>
      <span class="title-main">LANTERN HARBOR</span>
      <span class="title-small">PROMISE</span>
    </h2>
    <p class="synopsis">When Mira Dawson moves from her homeland in Japan to pursue her dream as an editor in the United States, she soon encounters a young Washingtonian artist. After being given the task to interview him, she becomes fixated on the mystique surrounding his past. She conjures her inner detective skills to embark on, what she thinks is, the biggest story of her career. But will her heart get in her way?</p>
  </section>

  <section class="panel spine">
    <div class="spine-emblem">
      <span class="emblem-square"></span>
      <span class="emblem-name">Lumen Press</span>
    </div>
    <p class="spine-author">Gareth Holloway</p>
    <p class="spine-title">The Lantern Harbor Promise</p>
  </section>

  <section class="panel front-cover">
    <div class="front-photo" role="img" aria-label="Close photo of a tree trunk with a chalk heart and two names drawn on the bark, fading into white at the top"></div>
    <h1 class="title-block">
      <span class="title-small">THE</span>
      <span class="title-main">LANTERN HARBOR</span>
      <span class="title-small">PROMISE</span>
    </h1>
    <p class="front-author">Gareth Holloway</p>
  </section>
</main>
</body>
</html>
```